Save our Business Card - We need your help

We need a fresh look on our business cards. We like it as it is, but it's not quite getting the 'wow' effect that we desire.
We're a tech startup building a cloud based solution for retailers consisting of Point of Sale, Inventory management and CRM.
The design should communicate a sense of a company that cares about the little things, design and relationships.
You can have a look at our website www.tillnest.com to get a feel for what we're like. Please feel free to message us for any further clarification
Target Market(s)
Our Customers are retail busines owners, cafe owners, other startups etc.
Industry/Entity Type
Building
Colors
Designer to choose colors to be used in the design.
Look and feel
Each slider illustrates characteristics of the customer's brand and the style your logo design should communicate.

```html
<!DOCTYPE html>
<html lang="en">
<head>
<meta charset="utf-8">
<title>TillNest Business Card</title>
<link href="https://fonts.googleapis.com/css2?family=Open+Sans:wght@400;600;700&display=swap" rel="stylesheet">
<style>
  :root {
    --bg: #e9e6e2;
    --orange-light: #f2873f;
    --orange: #ec6a22;
    --orange-dark: #d9531a;
    --yellow: #f7b733;
    --white: #ffffff;
    --line: #dedede;
    --back-mark: #f7e2cc;
    --shadow: rgba(60, 40, 20, 0.25);
  }
  * { margin: 0; padding: 0; box-sizing: border-box; }
  html, body { width: 1200px; height: 1023px; overflow: hidden; }
  body {
    background: var(--bg);
    font-family: "Open Sans", Arial, sans-serif;
    position: relative;
  }
  .card {
    position: absolute;
    left: 250px;
    width: 700px;
    height: 400px;
    border-radius: 4px;
    box-shadow: 0 10px 28px var(--shadow);
    overflow: hidden;
  }
  .card-front {
    top: 70px;
    background: linear-gradient(160deg, var(--orange-light) 0%, var(--orange) 55%, var(--orange-dark) 100%);
    color: var(--white);
  }
  .card-back {
    top: 545px;
    background: var(--white);
  }
  .rule {
    position: absolute;
    height: 4px;
    background: var(--line);
    border-radius: 2px;
  }
  .rule-top { left: 270px; top: 96px; width: 380px; }
  .rule-mid { left: 130px; top: 236px; width: 520px; }
  .rule-low { left: 130px; top: 298px; width: 200px; }
  .rule-bottom { left: 150px; top: 338px; width: 180px; }
  .holder {
    position: absolute;
    left: 130px;
    top: 104px;
  }
  .holder-name { font-size: 17px; line-height: 24px; font-weight: 600; }
  .holder-role { font-size: 12px; line-height: 16px; opacity: 0.85; }
  .brand {
    position: absolute;
    display: flex;
    align-items: center;
    gap: 14px;
  }
  .brand-square {
    width: 58px;
    height: 58px;
    background: var(--yellow);
  }
  .brand-name {
    font-weight: 700;
    font-size: 44px;
    line-height: 1;
    letter-spacing: -0.5px;
    color: var(--yellow);
  }
  .card-front .brand { left: 130px; top: 160px; }
  .contacts {
    position: absolute;
    left: 400px;
    top: 250px;
    font-size: 13px;
    line-height: 26px;
  }
  .contact-row { display: flex; align-items: center; gap: 10px; }
  .contact-row svg { width: 16px; height: 16px; flex: none; }
  .phone {
    position: absolute;
    left: 130px;
    top: 254px;
    font-size: 14px;
    line-height: 26px;
  }
  .back-tab {
    position: absolute;
    right: 0;
    top: 0;
  }
  .card-back .brand { left: 90px; top: 150px; }
  .card-back .brand-square { background: var(--orange); width: 90px; height: 90px; }
  .card-back .brand-name { color: var(--orange); font-size: 68px; }
  .back-mark {
    position: absolute;
    right: 60px;
    bottom: 50px;
    width: 70px;
    height: 70px;
    background: var(--back-mark);
  }
</style>
</head>
<body>

<section class="card card-front" aria-label="Business card front">
  <div class="rule rule-top"></div>
  <div class="holder">
    <div class="holder-name">Mara Ellison</div>
    <div class="holder-role">Manager</div>
  </div>
  <div class="brand">
    <div class="brand-square"></div>
    <div class="brand-name">TillNest</div>
  </div>
  <div class="rule rule-mid"></div>
  <div class="contacts">
    <div class="contact-row">
      <svg viewBox="0 0 16 16" aria-hidden="true"><rect width="16" height="16" rx="2" fill="#f7b733"/><circle cx="8" cy="8" r="4.5" fill="none" stroke="#ec6a22" stroke-width="1.3"/><line x1="3.5" y1="8" x2="12.5" y2="8" stroke="#ec6a22" stroke-width="1.1"/></svg>
      <span>www.tillnest.com</span>
    </div>
    <div class="contact-row">
      <svg viewBox="0 0 16 16" aria-hidden="true"><rect width="16" height="16" rx="2" fill="#f7b733"/><rect x="3" y="5" width="10" height="7" fill="none" stroke="#ec6a22" stroke-width="1.2"/><polyline points="3,5 8,9 13,5" fill="none" stroke="#ec6a22" stroke-width="1.2"/></svg>
      <span>hello@tillnest.com</span>
    </div>
  </div>
  <div class="phone contact-row">
    <svg viewBox="0 0 16 16" aria-hidden="true"><rect width="16" height="16" rx="2" fill="#f7b733"/><rect x="5" y="3" width="6" height="10" rx="1" fill="none" stroke="#ec6a22" stroke-width="1.2"/></svg>
    <span>00 987 654 321</span>
  </div>
  <div class="rule rule-low"></div>
  <div class="rule rule-bottom"></div>
</section>

<section class="card card-back" aria-label="Business card back">
  <svg class="back-tab" width="140" height="40" viewBox="0 0 140 40" aria-hidden="true">
    <polygon points="0,0 140,0 140,40" fill="#ec6a22"/>
  </svg>
  <div class="brand">
    <div class="brand-square"></div>
    <div class="brand-name">TillNest</div>
  </div>
  <div class="back-mark"></div>
</section>

</body>
</html>
```